Wine Label for a wine from Tuscany, Italy

We need a wine label for a white and red wine, can be the same label or can be somewhat differentiated with any variation you feel would be good.. These two wines come from Tuscany, Italy. Wine labels from Tuscany Italy tend to be traditional. We are open to traditional looking labels but also more modern, eye catching too. We want to convey a sense of elegance, importance, great wine. I am attaching some examples of labels we like from Tuscany, also a label that was designed for us recently by one of you, which we LOVE. No wine glasses, wine bottles or grapes featured on the label please. We tend to like the white background. No blue please.

Target Market(s)

More women than men purchase wine, but it needs to appeal to both sexes.

Requirements
Must have
• Wine Name: Corte l' or Corte l'
• Type/Varletal: Rosso Toscano (White is Vermentino)
• Vintage (year): 2018
• That is all the text we want on the label, thanks
Nice to have
• Clean, something that makes someone want to grab this wine bottle off the shelf!
Should not have
• Images of Wine glass, wine bottles, grapes
• Do not use the color blue please.

```html
<!DOCTYPE html>
<html lang="en">
<head>
<meta charset="utf-8">
<title>Corte l' – Wine Labels</title>
<link rel="stylesheet" href="https://fonts.googleapis.com/css2?family=Josefin+Sans:wght@300;400&display=swap">
<style>
  :root {
    --page: #ffffff;
    --label-paper: #f1f1f1;
    --ink: #1a1a1a;
    --rule: #1a1a1a;
    --vermentino: #a8985a;
    --rosso: #b3242c;
  }
  html, body {
    margin: 0;
    padding: 0;
    overflow: hidden;
    background: var(--page);
  }
  .canvas {
    position: relative;
    width: 1200px;
    height: 917px;
    background: var(--page);
    overflow: hidden;
    font-family: "Josefin Sans", sans-serif;
    color: var(--ink);
  }
  .label {
    position: absolute;
    margin: 0;
  }
  .label > * {
    position: absolute;
    left: 0;
    right: 0;
    margin: 0 auto;
    text-align: center;
    line-height: 1;
  }
  .label__name {
    font-weight: 300;
    white-space: nowrap;
  }
  .label__rule {
    height: 2px;
    background: var(--rule);
  }
  .label__varietal {
    font-weight: 400;
    text-transform: uppercase;
    letter-spacing: 0.04em;
  }
  .label__vintage {
    font-weight: 400;
    letter-spacing: 0.04em;
  }
  .label--white .label__varietal { color: var(--vermentino); }
  .label--red .label__varietal { color: var(--rosso); }

  /* Flat specimens, left column */
  .label--specimen { width: 300px; height: 200px; }
  .label--specimen .label__name { top: 0; font-size: 64px; }
  .label--specimen .label__rule { top: 128px; width: 46px; }
  .label--specimen .label__varietal { top: 141px; font-size: 11px; }
  .label--specimen .label__vintage { top: 156px; font-size: 10px; }
  .specimen-white { left: 110px; top: 182px; }
  .specimen-red { left: 110px; top: 559px; }

  /* Full labels, right side */
  .label--paper { top: 415px; height: 274px; background: var(--label-paper); }
  .label--paper .label__name { top: 112px; font-size: 46px; }
  .label--paper .label__rule { top: 217px; width: 36px; }
  .label--paper .label__varietal { top: 231px; font-size: 9px; }
  .label--paper .label__vintage { top: 244px; font-size: 8px; }
  .paper-white { left: 649px; width: 187px; }
  .paper-red { left: 911px; width: 190px; }
</style>
</head>
<body>
<main class="canvas">
  <section class="label label--specimen label--white specimen-white">
    <h1 class="label__name">Corte l'</h1>
    <div class="label__rule"></div>
    <p class="label__varietal">Vermentino</p>
    <p class="label__vintage">2018</p>
  </section>

  <section class="label label--specimen label--red specimen-red">
    <h2 class="label__name">Corte l'</h2>
    <div class="label__rule"></div>
    <p class="label__varietal">Rosso Toscano</p>
    <p class="label__vintage">2018</p>
  </section>

  <section class="label label--paper label--white paper-white">
    <h2 class="label__name">Corte l'</h2>
    <div class="label__rule"></div>
    <p class="label__varietal">Vermentino</p>
    <p class="label__vintage">2018</p>
  </section>

  <section class="label label--paper label--red paper-red">
    <h2 class="label__name">Corte l'</h2>
    <div class="label__rule"></div>
    <p class="label__varietal">Rosso Toscano</p>
    <p class="label__vintage">2018</p>
  </section>
</main>
</body>
</html>
```